Brand Voice Blueprint Book Cover Design

I'm about to publish the English version of my book on Brand Voice Blueprint. Name of the book is "Brand Voice Blueprint – How to untangle the online attention puzzle and leave your rivals behind". As a reference for colors and visual identity, I'm attaching the original book cover in Portuguese. I cannot reproduce the same cover due to my editor's copyright. I'm open to new fonts, font colors and illustrations that works well with the book title. I prefer a white or close to white solid or gradient background. I only need the front cover since the book will be published as an ebook format. The cover should show the title, subtitle, 3rd edition and my name "Tomas Veradello".

Target Market(s)

ebook publication on strategy / business

Industry/Entity Type

Business Management

Font styles to use
Sans Serif

Requirements
Must have
• The cover should show the title, subtitle, 3rd edition and my name "Tomas Veradello". White background. Should include a smart illustration that relates to the title. Illustration can be full of colors or more abstract. Use of shadows around the illustration is also ok. Keywords: social media, paradox, your company vs competitor, dialog, connection.
Nice to have
• Use the same visual identity from the first cover (attached).
Should not have
• Avoid the use of social media icons (from services like Chatterloom, Glimmerbox, etc.) or other kinds of icons such as phone, feed, wifi, etc.

```html
<!DOCTYPE html>
<html lang="en">
<head>
<meta charset="utf-8">
<title>Brand Voice Blueprint – Book Cover</title>
<link rel="stylesheet" href="https://fonts.googleapis.com/css2?family=Oswald:wght@400;500&family=Roboto+Condensed:wght@400;700&display=swap">
<style>
  :root {
    --paper: #ffffff;
    --accent-cyan: #1ea7dc;
    --edition-orange: #f39a1e;
    --ink: #4a4a4a;
    --arc-grey: #c9c9c9;
  }
  html, body {
    margin: 0;
    padding: 0;
    overflow: hidden;
    background: var(--paper);
  }
  .cover {
    position: relative;
    width: 849px;
    height: 1200px;
    background: var(--paper);
    overflow: hidden;
  }
  .edition-tab {
    position: absolute;
    top: 0;
    right: 0;
    width: 78px;
    height: 62px;
    background: var(--edition-orange);
    color: #fff;
    font-family: "Roboto Condensed", sans-serif;
    font-weight: 400;
    font-size: 17px;
    line-height: 1.05;
    text-align: center;
    padding-top: 8px;
    box-sizing: border-box;
    letter-spacing: 0.5px;
  }
  .edition-tab sup { font-size: 10px; }
  .signal-arcs {
    position: absolute;
    top: 0;
    left: 0;
  }
  .head-illustration {
    position: absolute;
    left: 360px;
    top: 60px;
    width: 470px;
    height: 500px;
    border-radius: 46% 40% 30% 48% / 50% 44% 40% 46%;
    background:
      radial-gradient(circle at 30% 30%, rgba(233, 76, 84, 0.55), transparent 45%),
      radial-gradient(circle at 70% 35%, rgba(30, 167, 220, 0.6), transparent 50%),
      radial-gradient(circle at 45% 75%, rgba(116, 190, 67, 0.55), transparent 45%),
      radial-gradient(circle at 80% 80%, rgba(243, 154, 30, 0.55), transparent 45%),
      radial-gradient(circle at 20% 60%, rgba(150, 90, 180, 0.45), transparent 45%),
      #f3f6f8;
  }
  .author {
    position: absolute;
    top: 536px;
    left: 0;
    width: 100%;
    text-align: center;
    font-family: "Roboto Condensed", sans-serif;
    font-weight: 700;
    font-size: 36px;
    letter-spacing: 1px;
    color: var(--ink);
    margin: 0;
  }
  .rule {
    position: absolute;
    left: 100px;
    width: 650px;
    height: 2px;
    background: var(--accent-cyan);
  }
  .rule-top { top: 590px; }
  .rule-bottom { top: 845px; }
  .title {
    position: absolute;
    top: 596px;
    left: 0;
    width: 100%;
    margin: 0;
    text-align: center;
    font-family: "Oswald", sans-serif;
    font-weight: 500;
    color: var(--accent-cyan);
    text-transform: uppercase;
    line-height: 1;
  }
  .title-line {
    display: block;
    font-size: 104px;
    letter-spacing: 5px;
    margin-bottom: 14px;
  }
  .subtitle {
    position: absolute;
    top: 862px;
    left: 0;
    width: 100%;
    margin: 0;
    text-align: center;
    font-family: "Roboto Condensed", sans-serif;
    font-weight: 400;
    font-size: 31px;
    line-height: 1.22;
    color: var(--ink);
    text-transform: uppercase;
    letter-spacing: 0.5px;
  }
</style>
</head>
<body>
<main class="cover">
  <svg class="signal-arcs" width="849" height="620" viewBox="0 0 849 620" aria-hidden="true">
    <g fill="none" stroke="var(--arc-grey)" stroke-width="2" stroke-dasharray="7 7">
      <circle cx="620" cy="330" r="230"/>
      <circle cx="620" cy="330" r="360"/>
      <circle cx="620" cy="330" r="500"/>
    </g>
  </svg>

  <div class="head-illustration" role="img" aria-label="Human head profile formed from many small colourful communication symbols, radiating outward"></div>

  <div class="edition-tab">3<sup>RD</sup> EDITION</div>

  <p class="author">TOMAS VERADELLO</p>

  <div class="rule rule-top"></div>
  <h1 class="title">
    <span class="title-line">Brand Voice</span>
    <span class="title-line">Blueprint</span>
  </h1>
  <div class="rule rule-bottom"></div>

  <p class="subtitle">How to untangle<br>the online attention puzzle<br>and leave your rivals behind</p>
</main>
</body>
</html>
```